Clear Strand Record Protocol Flyer

We need a flyer describing our initiative that seeks to develop and implement a standardized way of describing terrestrial fibre optic networks, which form the backbone of the Internet.
The primary audience that we are targeting is government and development decision makers and regulators, as well as businesses and groups involved in researching, planning, deploying and maintaining fibre optic infrastructure.

```html
<!DOCTYPE html>
<html lang="en">
<head>
<meta charset="utf-8">
<title>Clear Strand Record Protocol Flyer</title>
<link rel="stylesheet" href="https://fonts.googleapis.com/css2?family=Outfit:wght@300;400;600&display=swap">
<style>
  :root {
    --page: #f4f4f3;
    --sheet: #f9f9f9;
    --paper: #fafafa;
    --navy: #122a52;
    --ink: #111111;
    --yellow: #fbd84f;
    --blue: #2078b8;
    --deep-blue: #0d4c93;
    --night: #13233f;
  }
  * { margin: 0; padding: 0; box-sizing: border-box; }
  html, body {
    width: 848px;
    height: 1200px;
    overflow: hidden;
    background: var(--page);
    font-family: "Outfit", sans-serif;
  }
  .canvas {
    position: relative;
    width: 848px;
    height: 1200px;
  }
  .sheet {
    position: absolute;
    left: 14px;
    top: 0;
    width: 790px;
    height: 1074px;
    background: var(--sheet);
  }
  .panel {
    position: absolute;
    top: 93px;
    height: 776px;
    background: var(--paper);
    overflow: hidden;
    box-shadow: 0 12px 18px rgba(0, 0, 0, 0.12);
  }
  .panel-front { left: 41px; width: 352px; }
  .panel-back { left: 426px; width: 350px; }
  .panel svg.decor {
    position: absolute;
    left: 0;
    top: 0;
  }
  .front-title {
    position: absolute;
    left: 38px;
    top: 46px;
    font-size: 36px;
    line-height: 42px;
    font-weight: 600;
    color: var(--navy);
    letter-spacing: -0.3px;
    white-space: nowrap;
  }
  .front-lead {
    position: absolute;
    left: 53px;
    top: 276px;
    font-size: 18.5px;
    line-height: 27px;
    font-weight: 400;
    color: var(--navy);
    white-space: nowrap;
  }
  .front-lead strong { font-weight: 600; }
  .name-mark {
    position: absolute;
    left: 203px;
    top: 620px;
    width: 114px;
    height: 114px;
    border: 4px solid var(--navy);
    border-radius: 50%;
    display: flex;
    align-items: center;
    justify-content: center;
    font-size: 24px;
    font-weight: 600;
    color: var(--navy);
  }
  .back-title {
    position: absolute;
    left: 39px;
    top: 56px;
    font-size: 37px;
    line-height: 41px;
    font-weight: 600;
    color: var(--navy);
    white-space: nowrap;
  }
  .caption {
    position: absolute;
    left: 417px;
    top: 1008px;
    font-size: 25px;
    font-weight: 400;
    color: var(--ink);
    letter-spacing: 0.4px;
    white-space: nowrap;
  }
</style>
</head>
<body>
<div class="canvas">
  <div class="sheet"></div>

  <section class="panel panel-front">
    <svg class="decor" width="352" height="776" viewBox="0 0 352 776" aria-hidden="true">
      <path d="M0,234 C28,300 38,380 36,470 C34,610 90,740 226,776 L0,776 Z" fill="var(--yellow)"/>
      <path d="M0,495 C20,600 60,720 139,776 L0,776 Z" fill="var(--blue)"/>
      <path d="M0,669 C30,720 60,755 97,776 L0,776 Z" fill="var(--deep-blue)"/>
    </svg>
    <h1 class="front-title">Connecting<br>the World: The<br>Clear Strand<br>Record Protocol<br>(CSRP)</h1>
    <p class="front-lead">Everyone deserves access<br>to affordable and<br>reliable internet – <strong>matter</strong><br><strong>their location.</strong></p>
    <div class="name-mark">CSRP</div>
  </section>

  <section class="panel panel-back">
    <svg class="decor" width="350" height="776" viewBox="0 0 350 776">
      <path d="M209,0 C240,90 290,150 350,168 L350,0 Z" fill="var(--deep-blue)" aria-hidden="true"/>
      <path d="M275,0 C290,70 315,115 350,135 L350,0 Z" fill="var(--blue)" aria-hidden="true"/>
      <path d="M0,358 C40,362 75,372 100,392 L0,430 Z" fill="var(--yellow)" aria-hidden="true"/>
      <path d="M0,423 C60,385 150,380 215,410 C300,455 340,560 328,650 C322,705 305,745 288,776 L0,776 Z" fill="var(--night)" role="img" aria-label="Photo of yellow fibre optic patch cables with blue connectors"/>
    </svg>
    <h2 class="back-title">For<br>government<br>leaders,<br>regulators,<br>and<br>infrastructure<br>developers</h2>
  </section>

  <p class="caption">Front and back in front of your</p>
</div>
</body>
</html>
```